Skin Care Package Design

Hello,

I have a unique situation at hand. I already posted a project for this and we chose a winner but we ended up having trademark concerns so we need to modify the designs on the package.

We do not blame the designer in any way and we think that they did an incredible job. We have also chosen him as the winner and paid him so we have full right to share this and have 100% ownership of the design.

Our biggest competitor is Lumo Brisk Dot. We need to be careful not to have a design that is too close to theirs. I think the color red is fine in general, but we need to stay away from any shapes/designs that would be considered similar. They have a partial circle design on the corner and ours is to similar in our opinion - our mistake.

Our name is no longer Tidewell Co. It is now KELUNO or Keluno.

We need:
1. Tidewell Co removed and "KELUNO" or "Keluno" put in it's place. You do NOT have to leave the rectangle border. We do not have a design file or the logo yet. We like modern fonts.
2. Please remove the circular designs in the corners. It too closely resembles our competitors package. A square or some other unique concept would work. Feel free to use your imagination. We loved our current design because it's clean and simple but looks good.
3. Please don't mess with the text. We like it and the layout. Our focus is on the color/s and unique design that is going to replace the circle in the corners.
4. Please change "144" in the bottom right to "36".
5. The color red is still fine but we would be curious to see other colors like the green or blue that Dermita has or maybe a taupe. Use your imagination. We really want colors that pop and grab your attention. Feel free to use more than one color.

I have uploaded two images.
1. Lumo - Is our competitor's package.
2. Tidewell Co is our previous/current package design.

Package deminsions: 5”x3.4”x0.47”

Thanks! Good luck!

Target Market(s)

Male & female. We don't want the package design to be too masculine or too feminine.

Industry/Entity Type

Skin care, health & cosmetics.

Font styles to use
Sans Serif

Requirements
Must have
• You can search acne patch brands on Shopvane and see our competitors. We want ours to look better than Lumo Brisk Dot. They are the top seller. They have a simple and clean design but the red really grabs your eye. There are a ton of brands on the Shopvane page so it's important that the package looks good and the color/s catch your eye.

```html
<!DOCTYPE html>
<html lang="en">
<head>
<meta charset="UTF-8">
<title>Keluno – The Acne Patch</title>
<link href="https://fonts.googleapis.com/css2?family=Montserrat:wght@400;500;600;700&family=Poppins:wght@400;600;700&display=swap" rel="stylesheet">
<style>
  :root {
    --backdrop: #d9e4c1;
    --shadow: #b9d38e;
    --leaf-green: #6e9129;
    --kraft: #e8dcc2;
    --bamboo: #c8c49b;
    --ink: #353a23;
    --hole: #f6f8f1;
    --patch-blue: #b4d4df;
  }
  * { margin: 0; padding: 0; box-sizing: border-box; }
  html, body { width: 1200px; height: 1200px; overflow: hidden; background: var(--backdrop); }
  .canvas { position: relative; width: 1200px; height: 1200px; }

  .pack-shadow {
    position: absolute; left: 422px; top: 232px; width: 490px; height: 840px;
    background: var(--shadow); filter: blur(18px);
  }
  .hang-tab {
    position: absolute; left: 360px; top: 181px; width: 480px; height: 90px;
    background: var(--leaf-green);
  }
  .hang-hole { position: absolute; left: 204px; top: 17px; }

  .pack-face {
    position: absolute; left: 355px; top: 271px; width: 493px; height: 748px;
    background: var(--kraft); overflow: hidden;
  }
  .bamboo-art {
    position: absolute; left: 0; top: 0; width: 235px; height: 100%;
    background: linear-gradient(90deg, rgba(200,196,155,0.75) 0%, rgba(200,196,155,0.55) 60%, rgba(200,196,155,0) 100%);
  }

  .brand-name {
    position: absolute; left: 45px; top: 106px;
    font-family: 'Montserrat', sans-serif; font-weight: 600;
    font-size: 38px; letter-spacing: 4px; color: var(--ink);
  }

  .title { position: absolute; left: 43px; top: 222px; font-family: 'Poppins', sans-serif; line-height: 64px; font-size: 76px; }
  .title span { display: block; }
  .title .the { color: var(--leaf-green); font-weight: 400; letter-spacing: -1px; }
  .title .acne { color: var(--ink); font-weight: 700; letter-spacing: -1px; }
  .title .patch { color: var(--ink); font-weight: 400; letter-spacing: 1px; }

  .tagline-rule { position: absolute; left: 45px; top: 440px; width: 61px; height: 5px; background: var(--leaf-green); }
  .tagline {
    position: absolute; left: 117px; top: 430px;
    font-family: 'Poppins', sans-serif; font-weight: 600; font-size: 16px; color: var(--leaf-green);
  }
  .pointer { position: absolute; left: 310px; top: 392px; }

  .patch-art {
    position: absolute; left: 333px; top: 258px; width: 118px; height: 115px;
    border-radius: 50%;
    background: radial-gradient(circle at 60% 55%, #dde9ee 0%, var(--patch-blue) 70%, #7fbccd 100%);
  }

  .benefit {
    position: absolute; left: 45px; top: 468px;
    font-family: 'Montserrat', sans-serif; font-weight: 400; font-size: 31px; line-height: 34px; color: var(--ink);
  }
  .detail {
    position: absolute; left: 45px; top: 555px; width: 270px;
    font-family: 'Montserrat', sans-serif; font-weight: 400; font-size: 14.3px; line-height: 17px; color: var(--ink);
  }

  .count-badge { position: absolute; left: 325px; top: 553px; }
</style>
</head>
<body>
<div class="canvas">
  <div class="pack-shadow"></div>

  <div class="hang-tab">
    <svg class="hang-hole" width="72" height="50" viewBox="0 0 72 50">
      <path d="M16 50 A16 16 0 0 1 12 18 A14 14 0 0 1 20 14 A16 16 0 0 1 52 14 A14 14 0 0 1 60 18 A16 16 0 0 1 56 50 Z" fill="var(--hole)"/>
    </svg>
  </div>

  <div class="pack-face">
    <div class="bamboo-art" role="img" aria-label="Faint bamboo stalks and leaves illustration"></div>

    <div class="brand-name">KELUNO</div>

    <h1 class="title">
      <span class="the">THE</span>
      <span class="acne">ACNE</span>
      <span class="patch">PATCH</span>
    </h1>

    <div class="tagline-rule"></div>
    <div class="tagline">YOUR BLEMISH WIZARD</div>
    <svg class="pointer" width="80" height="60" viewBox="0 0 80 60">
      <path d="M2 54 C 34 53, 48 40, 55 18" fill="none" stroke="var(--leaf-green)" stroke-width="4.5" stroke-linecap="round"/>
      <path d="M49 20 L 60 6 L 64 24 Z" fill="var(--leaf-green)"/>
    </svg>

    <div class="patch-art" role="img" aria-label="Clear blue hydrocolloid patch with peeled corner"></div>

    <p class="benefit">Ideal for<br>surface spots</p>
    <p class="detail">Gently absorbs gunk in 6 - 8 hours &amp; approves the look of pimples overnight.</p>

    <svg class="count-badge" width="150" height="150" viewBox="0 0 150 150">
      <defs>
        <path id="badge-ring" d="M75 75 m -63 0 a 63 63 0 1 1 126 0 a 63 63 0 1 1 -126 0"/>
      </defs>
      <text font-family="Montserrat, sans-serif" font-weight="500" font-size="13" fill="var(--ink)" letter-spacing="3.2">
        <textPath href="#badge-ring" startOffset="2%">8 MM &amp; 12 MM SIZES ★ NON - DRYING ★</textPath>
      </text>
      <text x="75" y="88" text-anchor="middle" font-family="Poppins, sans-serif" font-weight="700" font-size="52" fill="var(--ink)">36</text>
      <text x="75" y="104" text-anchor="middle" font-family="Montserrat, sans-serif" font-weight="500" font-size="10" fill="var(--ink)">HYDROCOLLOID</text>
      <text x="75" y="115" text-anchor="middle" font-family="Montserrat, sans-serif" font-weight="500" font-size="10" fill="var(--ink)">PATCHES</text>
    </svg>
  </div>
</div>
</body>
</html>
```